Business Reporting Graph Illustration

I'm looking for a graphic design to created an illustration of a line chart I have two sample charts that I'd like elements of each combined together to create the project. Below is a link to learn more about this project. This should be designed using any product of the Adobe Suite.
Color Scheme is included within the below link. This will require 2 - 3 rounds of design before final completion.

https://www.brovex.com/file/QWTp7ksuHeLM382RK4Vxbd/Graphic-Design-Project

```html
<!DOCTYPE html>
<html lang="en">
<head>
<meta charset="utf-8">
<title>TV Ad Traffic Line Chart</title>
<link rel="stylesheet" href="https://fonts.googleapis.com/css2?family=Montserrat:wght@500;600&display=swap">
<style>
  :root {
    --bg: #ffffff;
    --line: #0d1b45;
    --axis: #8ea6cc;
    --axis-label: #4a6fa5;
    --ad: #f5a623;
  }
  html, body {
    margin: 0;
    padding: 0;
    width: 1200px;
    height: 675px;
    overflow: hidden;
    background: var(--bg);
  }
  .chart {
    display: block;
    width: 1200px;
    height: 675px;
    font-family: "Montserrat", sans-serif;
  }
  .ad-marker { stroke: var(--ad); stroke-width: 2; stroke-dasharray: 9 7; }
  .ad-box { fill: var(--bg); stroke: var(--ad); stroke-width: 2; }
  .ad-label { fill: var(--ad); font-size: 15px; font-weight: 600; text-anchor: middle; }
  .axis-line, .axis-tick { stroke: var(--axis); stroke-width: 1.5; }
  .axis-label { fill: var(--axis-label); font-size: 16px; font-weight: 600; text-anchor: middle; }
  .traffic-line { fill: none; stroke: var(--line); stroke-width: 2; stroke-linejoin: round; }
</style>
</head>
<body>
<svg class="chart" viewBox="0 0 1920 1080" role="img" aria-label="Line chart of traffic from 10:30 am to 2:15 pm with three TV ad windows marked">
  <g class="ad-markers">
    <line class="ad-marker" x1="121" y1="132" x2="121" y2="882"/>
    <line class="ad-marker" x1="145" y1="132" x2="145" y2="882"/>
    <line class="ad-marker" x1="402" y1="132" x2="402" y2="882"/>
    <line class="ad-marker" x1="442" y1="132" x2="442" y2="882"/>
    <line class="ad-marker" x1="1167" y1="132" x2="1167" y2="882"/>
    <line class="ad-marker" x1="1247" y1="132" x2="1247" y2="882"/>

    <rect class="ad-box" x="88" y="159" width="91" height="51"/>
    <text class="ad-label" x="133.5" y="180">TV Ad</text>
    <text class="ad-label" x="133.5" y="199">(3 Min)</text>

    <rect class="ad-box" x="377" y="159" width="91" height="51"/>
    <text class="ad-label" x="422.5" y="180">TV Ad</text>
    <text class="ad-label" x="422.5" y="199">(5 Min)</text>

    <rect class="ad-box" x="1162" y="159" width="91" height="51"/>
    <text class="ad-label" x="1207.5" y="180">TV Ad</text>
    <text class="ad-label" x="1207.5" y="199">(10 Min)</text>
  </g>

  <g class="axis">
    <line class="axis-line" x1="62" y1="882" x2="1862" y2="882"/>
    <g>
      <line class="axis-tick" x1="62" y1="872" x2="62" y2="892"/>
      <line class="axis-tick" x1="182" y1="872" x2="182" y2="892"/>
      <line class="axis-tick" x1="302" y1="872" x2="302" y2="892"/>
      <line class="axis-tick" x1="422" y1="872" x2="422" y2="892"/>
      <line class="axis-tick" x1="542" y1="872" x2="542" y2="892"/>
      <line class="axis-tick" x1="662" y1="872" x2="662" y2="892"/>
      <line class="axis-tick" x1="782" y1="872" x2="782" y2="892"/>
      <line class="axis-tick" x1="902" y1="872" x2="902" y2="892"/>
      <line class="axis-tick" x1="1022" y1="872" x2="1022" y2="892"/>
      <line class="axis-tick" x1="1142" y1="872" x2="1142" y2="892"/>
      <line class="axis-tick" x1="1262" y1="872" x2="1262" y2="892"/>
      <line class="axis-tick" x1="1382" y1="872" x2="1382" y2="892"/>
      <line class="axis-tick" x1="1502" y1="872" x2="1502" y2="892"/>
      <line class="axis-tick" x1="1622" y1="872" x2="1622" y2="892"/>
      <line class="axis-tick" x1="1742" y1="872" x2="1742" y2="892"/>
      <line class="axis-tick" x1="1862" y1="872" x2="1862" y2="892"/>
    </g>
    <g>
      <text class="axis-label" x="62" y="917">10:30 am</text>
      <text class="axis-label" x="182" y="917">10:45 am</text>
      <text class="axis-label" x="302" y="917">11:00 am</text>
      <text class="axis-label" x="422" y="917">11:15 am</text>
      <text class="axis-label" x="542" y="917">11:30 am</text>
      <text class="axis-label" x="662" y="917">11:45 am</text>
      <text class="axis-label" x="782" y="917">12:00 pm</text>
      <text class="axis-label" x="902" y="917">12:15 pm</text>
      <text class="axis-label" x="1022" y="917">12:30 pm</text>
      <text class="axis-label" x="1142" y="917">12:45 pm</text>
      <text class="axis-label" x="1262" y="917">1:00 pm</text>
      <text class="axis-label" x="1382" y="917">1:15 am</text>
      <text class="axis-label" x="1502" y="917">1:30 pm</text>
      <text class="axis-label" x="1622" y="917">1:45 pm</text>
      <text class="axis-label" x="1742" y="917">2:00 pm</text>
      <text class="axis-label" x="1862" y="917">2:15 pm</text>
    </g>
  </g>

  <g class="series">
    <polyline class="traffic-line" points="62,853 75,863 131,904 182,884 242,862 326,881 359,845 365,755 420,480 446,604 449,626 462,646 490,637 505,653 508,681 517,692 556,686 575,699 598,740 622,759 657,759 684,815 703,836 729,832 745,843 748,867 760,882 777,876 810,856 831,856 890,873 912,878 932,874 1000,838 1062,838"/>
    <polyline class="traffic-line" points="1068,869 1115,880 1149,830 1149,768 1187,600 1209,480 1235,600 1252,646 1280,637 1305,692 1344,685 1411,760 1442,761 1492,836 1521,832 1550,882 1596,857 1700,876 1789,837 1862,840"/>
  </g>
</svg>
</body>
</html>
```